Chatterly Design Project

To create a Chatterly design which matches my new company website:

www.ferntonassociates.com

And to install on Chatterly so that its up and running.

Original brief for website is at: http://jobs.pixelhive.com.au/job.aspx?Id=572104&draft=true

Upload the completed design to Chatterly.

It Company

```html
<!DOCTYPE html>
<html lang="en">
<head>
<meta charset="utf-8">
<title>Harbin test2 – Chatterly page</title>
<link href="https://fonts.googleapis.com/css2?family=Open+Sans:wght@400;600;700&family=Oswald:wght@300&display=swap" rel="stylesheet">
<style>
  :root {
    --page-bg: #e9ebf1;
    --topbar: #6d84b4;
    --topbar-edge: #4b67a1;
    --panel: #ffffff;
    --panel-edge: #c9cfdb;
    --link: #3b5998;
    --text: #333333;
    --muted: #8b90a0;
    --soft-line: #d3d8e3;
    --app-bg: #eef0f5;
    --button-bg: #f3f4f7;
    --primary: #5b74a8;
    --wood-dark: #2b2927;
    --wood-mid: #4a4744;
    --skin-light: #d8d5d2;
    --skin-mid: #a9a6a3;
    --cup-white: #f4f4f3;
  }
  * { box-sizing: border-box; margin: 0; padding: 0; }
  html, body { width: 1200px; height: 639px; overflow: hidden; }
  body {
    position: relative;
    background: var(--page-bg);
    font-family: "Open Sans", Arial, sans-serif;
    font-size: 10px;
    color: var(--text);
  }
  .abs { position: absolute; }
  .top-bar { left: 0; top: 0; width: 1200px; height: 24px; background: var(--topbar); border-bottom: 1px solid var(--topbar-edge); }

  .cover {
    left: 215px; top: 26px; width: 764px; height: 284px; overflow: hidden;
    background:
      radial-gradient(ellipse 150px 90px at 74% 0%, var(--cup-white) 0%, rgba(244,244,243,0.85) 55%, rgba(244,244,243,0) 100%),
      radial-gradient(ellipse 260px 120px at 52% 45%, rgba(216,213,210,0.95) 0%, rgba(169,166,163,0.6) 55%, rgba(169,166,163,0) 100%),
      radial-gradient(ellipse 220px 90px at 30% 12%, rgba(200,197,194,0.9) 0%, rgba(200,197,194,0) 100%),
      radial-gradient(ellipse 200px 140px at 88% 95%, rgba(190,187,184,0.85) 0%, rgba(190,187,184,0) 100%),
      linear-gradient(100deg, var(--wood-dark) 0%, var(--wood-mid) 40%, var(--wood-dark) 75%, var(--wood-mid) 100%);
  }
  .cover-brand { right: 16px; top: 136px; color: #fff; display: flex; align-items: center; gap: 7px; }
  .cover-brand .mark { width: 26px; height: 26px; border-radius: 50%; background: #fff; }
  .cover-brand .name { font-size: 14px; font-weight: 400; line-height: 15px; }
  .cover-brand .tagline { display: block; font-size: 5px; letter-spacing: 2.2px; line-height: 7px; }

  .header-panel {
    left: 215px; top: 310px; width: 764px; height: 168px;
    background: var(--panel); border: 1px solid var(--panel-edge); border-top: none; border-radius: 0 0 3px 3px;
  }
  .profile-pic {
    left: 235px; top: 268px; width: 153px; height: 101px;
    background: var(--panel); border: 1px solid var(--panel-edge); padding: 4px;
  }
  .profile-pic .inner {
    width: 100%; height: 100%;
    background: linear-gradient(180deg, var(--wood-mid) 0%, var(--wood-dark) 100%);
    display: flex; justify-content: center; padding-top: 14px;
    color: #f59a2a; font-size: 20px; font-weight: 700;
  }
  .page-name { left: 401px; top: 322px; font-size: 18px; font-weight: 700; color: #1c2a47; }
  .page-likes { left: 401px; top: 346px; font-size: 9px; color: var(--muted); }

  .btn {
    border: 1px solid #999; border-radius: 2px; background: var(--button-bg);
    font-weight: 700; font-size: 11px; color: var(--text);
    display: flex; align-items: center; justify-content: center; gap: 4px;
  }
  .btn-liked { left: 851px; top: 324px; width: 58px; height: 22px; }
  .btn-gear { left: 918px; top: 324px; width: 39px; height: 22px; color: #555; }

  .app-about { left: 216px; top: 378px; width: 293px; height: 65px; background: var(--app-bg); border-right: 1px solid var(--soft-line); }
  .info-icon { left: 24px; top: 18px; }
  .about-label { left: 39px; top: 70px; font-size: 10px; color: var(--link); }
  .app-tile { top: 378px; width: 100px; height: 65px; display: flex; align-items: center; justify-content: flex-end; padding-right: 7px;
    font-family: "Oswald", "Arial Narrow", sans-serif; font-weight: 300; font-size: 24px; color: #fff; }
  .tile-photos { left: 517px; background: linear-gradient(165deg, #2a2826 0%, #3b3936 45%, #cfccc9 62%, #efeeec 100%); }
  .tile-about { left: 623px; background: linear-gradient(160deg, #2e2c2a 0%, #45423f 55%, #242321 100%); }
  .tile-website { left: 731px; background: linear-gradient(150deg, #2c2b2a 0%, #55524f 55%, #8d8a87 100%); }
  .tile-blog { left: 837px; background: linear-gradient(150deg, #9c9996 0%, #c9c6c3 55%, #e2e0de 100%); }
  .tile-more { left: 945px; width: 33px; background: var(--app-bg); }
  .app-label { top: 451px; font-size: 10px; color: var(--link); }

  .timeline-line { left: 597px; top: 478px; width: 2px; height: 161px; background: #cdd3df; }
  .timeline-dot { left: 594px; top: 560px; width: 8px; height: 8px; border-radius: 50%; background: #cdd3df; }
  .highlights { left: 563px; top: 493px; width: 68px; height: 20px; background: var(--page-bg); border: 1px solid #c4cad6; border-radius: 2px;
    font-size: 10px; color: var(--muted); display: flex; align-items: center; justify-content: center; gap: 4px; }

  .composer { left: 215px; top: 539px; width: 369px; height: 68px; background: var(--panel); border: 1px solid var(--panel-edge); border-radius: 3px; }
  .composer-tabs { display: flex; height: 36px; align-items: center; font-size: 11px; font-weight: 700; color: var(--link); }
  .composer-tab { display: flex; align-items: center; gap: 5px; padding: 0 14px; border-right: 1px solid #e3e6ec; }
  .composer-tab:first-child { color: var(--text); }
  .composer-tab:last-child { border-right: none; }
  .composer-input { margin: 0 5px; height: 26px; border: 1px solid #bdc7d8; padding: 5px 5px; font-size: 11px; color: #6b6f78; }

  .friends { left: 610px; top: 539px; width: 368px; height: 110px; background: var(--panel); border: 1px solid var(--panel-edge); border-radius: 3px; }
  .friends-count { left: 13px; top: 11px; font-size: 22px; font-weight: 700; color: var(--link); }
  .friends-title { left: 34px; top: 15px; font-size: 10px; font-weight: 700; color: var(--link); }
  .friends-sub { left: 34px; top: 27px; font-size: 9px; color: var(--muted); }
  .friends-rule { left: 13px; top: 47px; width: 341px; height: 1px; background: #e3e6ec; }
  .friend-thumbs { left: 13px; top: 51px; display: flex; gap: 1px; }
  .friend-thumbs span { width: 33px; height: 33px; }
  .thumb-1 { background: linear-gradient(160deg, #6f7b58, #3e4733 60%, #2a2f22); }
  .thumb-2 { background: linear-gradient(180deg, #1f2a1c, #5a6a48 55%, #9aa58a); }
  .thumb-3 { background: linear-gradient(160deg, #e0d6c8, #b08a68 55%, #6b5140); }
  .thumb-4 { background: linear-gradient(150deg, #8fb3c9, #6f8f6a 55%, #3f5a48); }
  .thumb-5 { background: linear-gradient(170deg, #5d87c2, #b8cde3 55%, #eef3f8); }
  .thumb-6 { background: linear-gradient(160deg, #f2e6dc, #c98a62 55%, #7a4a32); }

  .create-page { left: 991px; top: 36px; width: 74px; height: 19px; background: var(--primary); border: 1px solid #3b5998; border-radius: 2px;
    color: #fff; font-weight: 700; font-size: 10px; display: flex; align-items: center; justify-content: center; }
  .side-rule { left: 990px; top: 66px; width: 210px; height: 1px; background: #d3d8e3; }
  .scrubber { left: 991px; top: 74px; }
  .scrubber li { list-style: none; height: 21px; line-height: 19px; padding-left: 9px; border-left: 3px solid #d3d8e3; font-size: 10px; color: #9ba2b3; }
  .scrubber li.current { border-left-color: var(--primary); color: var(--primary); font-weight: 700; }

  .ad-heading { left: 990px; top: 488px; font-size: 10px; font-weight: 700; color: #666; }
  .ad-rule { left: 990px; top: 504px; width: 210px; height: 1px; background: #d3d8e3; }
  .ad-title { left: 990px; top: 508px; font-size: 10px; font-weight: 700; color: var(--link); }
  .ad-image { left: 990px; top: 525px; width: 90px; height: 67px; background: linear-gradient(180deg, #aebfd3 0%, #d4dde7 60%, #b9c7d6 100%);
    display: flex; align-items: center; justify-content: center; font-size: 11px; font-weight: 700; color: #2e4a3a; }
  .ad-like { left: 990px; top: 597px; font-size: 9px; color: var(--muted); display: flex; align-items: center; gap: 3px; }
  .ad-like b { color: var(--link); font-weight: 400; }
  .advertise { left: 991px; top: 615px; width: 114px; height: 19px; background: var(--button-bg); border: 1px solid #999;
    font-weight: 700; font-size: 10px; display: flex; align-items: center; justify-content: center; }
</style>
</head>
<body>
  <div class="abs top-bar"></div>

  <div class="abs cover" role="img" aria-label="Black and white photo of two clasped hands on a dark wooden table beside a white coffee cup">
    <div class="abs cover-brand">
      <span class="mark"></span>
      <span><span class="name">Fernton Associates</span><span class="tagline">BUSINESS ADVISORS</span></span>
    </div>
  </div>

  <div class="abs header-panel">
    <div class="abs app-about" style="left:0;top:67px;">
      <svg class="abs info-icon" width="32" height="32" viewBox="0 0 32 32" aria-hidden="true">
        <circle cx="16" cy="16" r="15" fill="#dde2ec" stroke="#c6cdda"/>
        <circle cx="16" cy="9.5" r="2" fill="#9aa3b8"/>
        <rect x="14.3" y="13" width="3.4" height="11" fill="#9aa3b8"/>
      </svg>
      <span class="abs about-label">About</span>
    </div>
  </div>

  <div class="abs profile-pic"><div class="inner">Fernton</div></div>
  <div class="abs page-name">Harbin test2</div>
  <div class="abs page-likes">13 likes</div>

  <div class="abs btn btn-liked">
    <svg width="9" height="8" viewBox="0 0 9 8" aria-hidden="true"><path d="M1 4l2.5 2.5L8 1" fill="none" stroke="#555" stroke-width="1.6"/></svg>Liked
  </div>
  <div class="abs btn btn-gear">
    <svg width="10" height="10" viewBox="0 0 10 10" aria-hidden="true"><circle cx="5" cy="5" r="3.2" fill="none" stroke="#555" stroke-width="2" stroke-dasharray="1.6 1"/></svg>
    <svg width="8" height="5" viewBox="0 0 8 5" aria-hidden="true"><path d="M0 0h8L4 5z" fill="#5b74a8"/></svg>
  </div>

  <div class="abs app-tile tile-photos" role="img" aria-label="Close-up photo of a hand on a dark table"></div>
  <div class="abs app-tile tile-about">about</div>
  <div class="abs app-tile tile-website">website</div>
  <div class="abs app-tile tile-blog">blog</div>
  <div class="abs app-tile tile-more"></div>

  <span class="abs app-label" style="left:517px;">Photos</span>
  <span class="abs app-label" style="left:623px;">Photos</span>
  <span class="abs app-label" style="left:731px;">About Me</span>
  <span class="abs app-label" style="left:837px;">Brightcraft</span>

  <div class="abs timeline-line"></div>
  <div class="abs timeline-dot"></div>
  <div class="abs highlights">Highlights
    <svg width="7" height="4" viewBox="0 0 7 4" aria-hidden="true"><path d="M0 0h7L3.5 4z" fill="#8b90a0"/></svg>
  </div>

  <div class="abs composer">
    <div class="composer-tabs">
      <span class="composer-tab"><svg width="12" height="12" viewBox="0 0 12 12" aria-hidden="true"><rect x="1" y="1" width="10" height="10" fill="#f6d46b" stroke="#c9a23a"/><path d="M3 4h6M3 6h6M3 8h4" stroke="#a07d1f"/></svg>Status</span>
      <span class="composer-tab"><svg width="13" height="12" viewBox="0 0 13 12" aria-hidden="true"><rect x="0.5" y="1.5" width="12" height="9" fill="#f3e6c9" stroke="#8a6b3a"/><rect x="3" y="3.5" width="7" height="5" fill="#b88a4a"/></svg>Photo / Video</span>
      <span class="composer-tab"><svg width="12" height="12" viewBox="0 0 12 12" aria-hidden="true"><rect x="0.5" y="1.5" width="11" height="10" fill="#fff" stroke="#888"/><rect x="0.5" y="1.5" width="11" height="3" fill="#c0392b"/></svg>Event, Milestone +</span>
    </div>
    <div class="composer-input">Write something...</div>
  </div>

  <div class="abs friends">
    <span class="abs friends-count">6</span>
    <span class="abs friends-title">Friends</span>
    <span class="abs friends-sub">Like Harbin test2</span>
    <div class="abs friends-rule"></div>
    <div class="abs friend-thumbs" role="img" aria-label="Six small friend profile photos">
      <span class="thumb-1"></span>
      <span class="thumb-2"></span>
      <span class="thumb-3"></span>
      <span class="thumb-4"></span>
      <span class="thumb-5"></span>
      <span class="thumb-6"></span>
    </div>
  </div>

  <div class="abs create-page">Create Page</div>
  <div class="abs side-rule"></div>
  <ul class="abs scrubber">
    <li class="current">Now</li>
    <li>October</li>
    <li>Born</li>
  </ul>

  <div class="abs ad-heading">See Your Ad Here</div>
  <div class="abs ad-rule"></div>
  <div class="abs ad-title">Harbin test2</div>
  <div class="abs ad-image">Stallway</div>
  <div class="abs ad-like">
    <svg width="10" height="10" viewBox="0 0 10 10" aria-hidden="true"><path d="M1 4h2v5H1zM3.5 4L5.5 1c1 0 1.3.6 1 1.6L6 4h2.5c.6 0 1 .5.8 1.1L8.4 8.4c-.1.4-.5.6-.9.6H3.5z" fill="#5b74a8"/></svg>
    <b>Like</b> · Marek Dall likes this.
  </div>
  <div class="abs advertise">Advertise Your Page</div>
</body>
</html>
```